Interior Design/ decoration business card design

This card is for my Interior Design and Decoration business and later I will also be selling homewares. I would like the card to be very simple in design and like either white, duck egg blue , aquas or metallics on a flat mat card excellent quality card. It needs to be well designed as that is my field. I dont like fuss, the simpler the better. I would like a styalised wren under the name wren if possible. SIMPLE, STYLISH, CLASSIC, TASTEFUL

Target Market(s)

40 + year olds who are building or rennovating.

Industry/Entity Type

Business

Contact Information for Business Card

Wren
styling, design, homeware

Marnie Tolland
p 0427316958
e marnie@wrenliving.com.au
w wrenliving.com.au

Requirements
Must have
• very simple, stylish, classic, sophisticated. Simple and easy to read text that is a print similar to attached image. I like simple round A's though not as in attached image.

Double sided. It wont save as double sided for some reason!!
Should not have
• not too much colour, No animated / cartoon pictures.

```html
<!DOCTYPE html>
<html lang="en">
<head>
<meta charset="utf-8">
<title>Wren business card</title>
<link href="https://fonts.googleapis.com/css2?family=Quicksand:wght@400;500;600&display=swap" rel="stylesheet">
<style>
  :root {
    --backdrop: #bdb9b6;
    --duck-egg: #b9d8d5;
    --paper: #ffffff;
    --bark: #44372f;
    --aqua-ink: #9fcfcb;
    --tagline: #ffffff;
  }
  * { margin: 0; padding: 0; box-sizing: border-box; }
  html, body {
    width: 1200px;
    height: 1000px;
    overflow: hidden;
    background: var(--backdrop);
    font-family: "Quicksand", sans-serif;
  }
  .sheet {
    position: relative;
    width: 1200px;
    height: 1000px;
  }
  .card {
    position: absolute;
    top: 368px;
    width: 436px;
    height: 264px;
    box-shadow: 2px 3px 6px rgba(0, 0, 0, 0.35);
  }
  .card--front { left: 148px; background: var(--duck-egg); }
  .card--back { left: 617px; background: var(--paper); }

  .brand {
    position: absolute;
    font-weight: 400;
    line-height: 1;
    letter-spacing: 0.5px;
  }
  .card--front .brand {
    left: 224px;
    top: 110px;
    font-size: 44px;
    color: var(--bark);
  }
  .tagline {
    position: absolute;
    right: 42px;
    top: 222px;
    font-size: 16px;
    font-weight: 400;
    color: var(--tagline);
    word-spacing: 10px;
    letter-spacing: 0.2px;
  }

  .contact {
    position: absolute;
    left: 27px;
    top: 162px;
    font-size: 13.5px;
    line-height: 1;
    color: var(--bark);
  }
  .contact__name { font-weight: 600; font-size: 14.5px; margin-bottom: 5px; }
  .contact__email { color: var(--aqua-ink); margin-bottom: 10px; }
  .contact__phone { margin-bottom: 6px; }
  .contact__web { }

  .card--back .brand {
    left: 290px;
    top: 186px;
    font-size: 28px;
    color: var(--aqua-ink);
  }
</style>
</head>
<body>
  <main class="sheet">
    <section class="card card--front" aria-label="Card front">
      <div class="brand">wren</div>
      <div class="tagline">decoration styling homeware</div>
    </section>

    <section class="card card--back" aria-label="Card back">
      <div class="contact">
        <p class="contact__name">Marnie Tolland</p>
        <p class="contact__email">marnie@wrenliving.com.au</p>
        <p class="contact__phone">042 731 6958</p>
        <p class="contact__web">www.wrenliving.com.au</p>
      </div>
      <div class="brand">wren</div>
    </section>
  </main>
</body>
</html>
```